Packaging for baby product company

We require a packaging design for our new baby brush kit we are launching.

I have attached the logo pernwix.pdf (when winner is chosen we can replace with .ai file) for our brand and images of the items inside the packaging. The packaging is two pieces as per the ref1 image. it shows the bottom part of the packaging so please take into consideration for design that we need lid and bottom.

the design should communicate comfort and reliability to our audience of parents.

New parents

Baby

```html
<!DOCTYPE html>
<html lang="en">
<head>
<meta charset="utf-8">
<title>pernwix Baby Brush Kit – Front Panel</title>
<link rel="stylesheet" href="https://fonts.googleapis.com/css2?family=Fredoka:wght@600&family=Ribeye&family=Open+Sans:wght@400&family=Quicksand:wght@500&display=swap">
<style>
  :root {
    --page-bg: #b3bac1;
    --box-blue: #8ec3dc;
    --chevron-grey: #8894a0;
    --cream: #efeee7;
    --band-grey: #6d7a85;
    --stitch: #6f7a84;
    --title-pink: #d2549a;
    --title-outline: #9fd0ea;
    --feature-blue: #6f9fd2;
    --logo-purple: #8a63b8;
    --ink: #3a3a3a;
    --flower-tone: #e9b8cf;
  }
  * { margin: 0; padding: 0; box-sizing: border-box; }
  html, body { width: 1200px; height: 1052px; overflow: hidden; }
  body { background: var(--page-bg); position: relative; font-family: "Open Sans", sans-serif; }

  .front-panel {
    position: absolute; left: 310px; top: 43px; width: 580px; height: 966px;
    background: var(--box-blue); overflow: hidden;
  }
  .chevron-field {
    position: absolute; left: 0; top: 0; width: 100%; height: 490px;
    background: linear-gradient(180deg, #c9d4dc 0%, #b7c6d2 100%);
  }
  .dot-field {
    position: absolute; left: 0; top: 530px; width: 100%; height: 436px;
    background: linear-gradient(180deg, #a7cfe2 0%, #9ccbe0 100%);
  }
  .band {
    position: absolute; left: 0; top: 470px; width: 100%; height: 60px;
    background: var(--band-grey);
  }
  .label-frame { position: absolute; left: 0; top: 0; width: 580px; height: 966px; }

  .brand {
    position: absolute; left: 0; width: 100%; top: 290px; text-align: center;
    font-family: "Fredoka", sans-serif; font-weight: 600; font-size: 78px;
    color: var(--logo-purple); line-height: 1;
  }
  .brand-sub {
    position: absolute; left: 300px; top: 376px;
    font-family: "Quicksand", sans-serif; font-size: 12px; letter-spacing: 3px; color: var(--ink);
  }
  .product-title {
    position: absolute; left: 0; width: 100%; top: 462px; text-align: center;
    font-family: "Ribeye", serif; font-size: 54px; color: var(--title-pink);
    -webkit-text-stroke: 1px var(--title-outline); paint-order: stroke fill;
  }
  .features {
    position: absolute; left: 0; width: 100%; top: 588px; text-align: center; list-style: none;
    font-family: "Open Sans", sans-serif; font-size: 24px; line-height: 42px;
    color: var(--feature-blue); letter-spacing: 0.5px;
  }
  .flowers {
    position: absolute; width: 70px; height: 90px; border-radius: 40%;
    background: radial-gradient(circle, var(--flower-tone) 0%, rgba(233,184,207,0.25) 70%, transparent 72%);
  }
  .flowers--left { left: 110px; top: 600px; }
  .flowers--right { left: 395px; top: 600px; }
  .description {
    position: absolute; left: 150px; width: 280px; top: 730px;
    font-size: 11.5px; line-height: 15px; color: var(--ink); text-align: justify;
  }
</style>
</head>
<body>
  <section class="front-panel">
    <div class="chevron-field" role="img" aria-label="Grey, blue and cream zigzag chevron pattern"></div>
    <div class="dot-field" role="img" aria-label="Light blue background with large cream polka dots"></div>
    <div class="band"></div>

    <svg class="label-frame" viewBox="0 0 580 966" aria-hidden="true">
      <path d="M110 230 Q140 230 150 200 L270 200 L290 168 L310 200 L430 200 Q440 230 470 230
               L470 810 Q440 810 430 840 L310 840 L290 872 L270 840 L150 840 Q140 810 110 810 Z"
            fill="var(--cream)" stroke="#d9d8cf" stroke-width="2"/>
      <path d="M122 242 Q150 240 158 212 L274 212 L290 186 L306 212 L422 212 Q430 240 458 242
               L458 798 Q430 800 422 828 L306 828 L290 854 L274 828 L158 828 Q150 800 122 798 Z"
            fill="none" stroke="var(--stitch)" stroke-width="1.5" stroke-dasharray="4 3"/>
    </svg>

    <div class="brand">pernwix</div>
    <div class="brand-sub">COLLECTION</div>
    <h1 class="product-title">Baby Brush Kit</h1>

    <div class="flowers flowers--left" role="img" aria-label="Small pastel flower illustrations"></div>
    <div class="flowers flowers--right" role="img" aria-label="Small pastel flower illustrations"></div>

    <ul class="features">
      <li>MASSAGE</li>
      <li>ANNUAL AGE</li>
      <li>ENVIRONMENTAL</li>
    </ul>

    <p class="description">Safety Soft Wooden Baby Hair Brush and Wooden Comb Set health care Baby Grooming Sets for Newborn baby &amp; Toddlers</p>
  </section>
</body>
</html>
```